Italian Dinning Table and wardrobe Selling Website

We need a website design for a reputable furniture company deals in the manufacture of Italian dinning tables and wardrobe. We provide our services to USA based customers.

The categories of the website are
- Home page
- Product page
- The page where all the items are sold
- The shopping cart page

The website is required to have several areas of products with prices that can be added to shopping cart.
Also the website should have customer login facility along with privacy policy, contact us, about us and terms of use
Preferred colors are brown, black and pink,

It Company

```html
<!DOCTYPE html>
<html lang="en">
<head>
<meta charset="utf-8">
<title>Tavolora — Italian Dining Tables &amp; Wardrobes</title>
<link href="https://fonts.googleapis.com/css2?family=Jost:wght@300;400;500;600;700&family=Playfair+Display:ital@1&display=swap" rel="stylesheet">
<style>
  :root {
    --page-bg: #ffffff;
    --ink: #1e1b19;
    --muted: #8b8682;
    --line: #ececec;
    --brown: #8b6a52;
    --rose: #e0555f;
    --white: #ffffff;
  }
  * { box-sizing: border-box; margin: 0; padding: 0; }
  html, body { width: 1200px; height: 868px; overflow: hidden; }
  body {
    background: var(--page-bg);
    color: var(--ink);
    font-family: "Jost", sans-serif;
    position: relative;
  }

  /* utility bar */
  .utility-bar {
    position: absolute; left: 0; top: 0; width: 1200px; height: 38px;
    border-bottom: 1px solid var(--line);
    display: flex; align-items: center; padding: 0 24px;
    font-size: 11px; color: var(--ink);
  }
  .utility-bar .util-left { display: flex; gap: 26px; }
  .utility-bar .util-item { display: flex; align-items: center; gap: 6px; }
  .utility-bar svg { width: 10px; height: 10px; }
  .search-field {
    position: absolute; left: 904px; top: 12px;
    display: flex; align-items: center; gap: 6px;
    color: #b9b5b1; font-size: 11px;
  }
  .account-link {
    position: absolute; left: 1108px; top: 12px;
    display: flex; align-items: center; gap: 6px;
  }

  /* main navigation */
  .main-nav {
    position: absolute; left: 0; top: 74px; width: 1200px; height: 50px;
    font-size: 10.5px; letter-spacing: 1.2px; color: var(--muted); font-weight: 500;
  }
  .main-nav a { position: absolute; top: 18px; text-decoration: none; color: inherit; }
  .brand-name {
    position: absolute; left: 0; width: 1200px; top: 0; text-align: center;
    font-size: 38px; font-weight: 400; color: var(--ink); letter-spacing: 0.5px;
  }
  .cart-icon { position: absolute; left: 944px; top: 16px; width: 14px; height: 14px; }

  /* hero */
  .hero-photo {
    position: absolute; left: 276px; top: 162px; width: 850px; height: 336px;
    background: linear-gradient(100deg, #8d8172 0%, #b4a690 30%, #7a6d5f 55%, #5b5048 80%, #6e6257 100%);
  }
  .deal-label {
    position: absolute; left: 76px; top: 292px;
    font-family: "Playfair Display", serif; font-style: italic;
    font-size: 13px; color: var(--muted);
  }
  .deal-title {
    position: absolute; left: 70px; top: 312px; width: 508px; height: 48px;
    background: var(--white); padding: 5px 6px;
    font-size: 29px; font-weight: 500; white-space: nowrap;
  }
  .deal-title .designer { font-weight: 600; font-style: italic; text-decoration: underline; text-underline-offset: 4px; }
  .deal-summary {
    position: absolute; left: 70px; top: 369px; width: 384px; height: 64px;
    background: var(--white); padding: 6px 12px 6px 8px;
    font-size: 11px; line-height: 1.35; color: var(--ink);
  }
  .price-label { position: absolute; left: 76px; top: 444px; font-size: 11px; color: var(--ink); }
  .price { position: absolute; left: 76px; top: 458px; font-size: 24px; font-weight: 400; }
  .discover-button {
    position: absolute; left: 76px; top: 504px; width: 178px; height: 33px;
    background: var(--brown); color: var(--white);
    font-size: 10px; letter-spacing: 2px; font-weight: 600;
    display: flex; align-items: center; justify-content: center;
  }

  /* together band */
  .together-band {
    position: absolute; left: 76px; top: 582px; width: 1050px; height: 286px;
    background: var(--rose); color: var(--white); text-align: center;
  }
  .together-band h2 { margin-top: 60px; font-size: 27px; font-weight: 500; }
  .together-band p {
    width: 560px; margin: 12px auto 0; font-size: 12.5px; line-height: 1.45;
  }
</style>
</head>
<body>
  <header class="utility-bar">
    <div class="util-left">
      <span class="util-item"><svg viewBox="0 0 10 10"><circle cx="5" cy="5" r="4" fill="none" stroke="#555"/><path d="M1 5h8M5 1c2 2 2 6 0 8M5 1c-2 2-2 6 0 8" fill="none" stroke="#555" stroke-width=".7"/></svg>English</span>
      <span class="util-item">$ USD</span>
      <span class="util-item"><svg viewBox="0 0 10 10"><rect x="1" y="2" width="8" height="6" fill="none" stroke="#555"/><path d="M1 2l4 3 4-3" fill="none" stroke="#555"/></svg>Contact</span>
      <span class="util-item">? Assistance</span>
    </div>
    <div class="search-field"><svg viewBox="0 0 10 10"><circle cx="4" cy="4" r="3" fill="none" stroke="#999"/><path d="M6.2 6.2L9 9" stroke="#999"/></svg>Enter search key</div>
    <div class="account-link"><svg viewBox="0 0 10 10"><circle cx="5" cy="3" r="2" fill="#555"/><path d="M1 10c0-3 8-3 8 0z" fill="#555"/></svg>My Account</div>
  </header>

  <nav class="main-nav">
    <a href="#" style="left:196px">SHOP</a>
    <a href="#" style="left:250px">CATALOGUES</a>
    <a href="#" style="left:346px">COLLECTIONS</a>
    <div class="brand-name">Tavolora</div>
    <a href="#" style="left:812px">STORES</a>
    <a href="#" style="left:878px">BRAND</a>
    <svg class="cart-icon" viewBox="0 0 14 14"><path d="M1 2h2l2 7h7l1.5-5H4" fill="none" stroke="#8b8682" stroke-width="1.3"/><circle cx="6" cy="12" r="1" fill="#8b8682"/><circle cx="11" cy="12" r="1" fill="#8b8682"/></svg>
  </nav>

  <main>
    <div class="hero-photo" role="img" aria-label="Walnut dining table with glass centre insert and leather chairs in a styled dining room"></div>
    <p class="deal-label">Deal of the day</p>
    <h1 class="deal-title">“The Brook table”, by <span class="designer">Lorenzo Valtieri</span></h1>
    <p class="deal-summary">A statement piece of any living space. The fascinating central glass insert runs through the entire length of this truly unique table. The top is available in Canaletto walnut or burned oak.</p>
    <p class="price-label">Starting at</p>
    <p class="price">$4,924</p>
    <a class="discover-button">DISCOVER</a>

    <section class="together-band">
      <h2>For sharing meals &amp; being together</h2>
      <p>Neque porro quisquam est qui dolorem ipsum quia dolor sit amet, consectetur, adipisci velit. Lorem ipsum dolor sit amet, consectetur adipiscing elit, sed do eiusmod tempor incididunt ut labore et dolore magna aliqua.</p>
    </section>
  </main>
</body>
</html>
```